menu board design: harbor burger

we are a burger restaurant.
we need to re design our menu board to fit within the new design of the restaurant. we are after something simple and easy to read. the overall look and feel of the design should be inline with the design of the shop.

Target Market(s)

18-40 male and female

Colors

Designer to choose colors to be used in the design.

Requirements
Must have
• easy to read. good layout. white background. branding included in design.

```html
<!DOCTYPE html>
<html lang="en">
<head>
<meta charset="utf-8">
<title>Harbor Burger Menu Board</title>
<link href="https://fonts.googleapis.com/css2?family=Jost:wght@700&family=Montserrat:wght@700;800;900&display=swap" rel="stylesheet">
<style>
  :root {
    --ink: #111111;
    --accent: #e0147c;
    --accent-soft: #f8d2e5;
    --paper: #ffffff;
  }
  * { box-sizing: border-box; margin: 0; padding: 0; }
  html, body { width: 1200px; height: 600px; overflow: hidden; background: var(--paper); }
  .board {
    position: relative; width: 1200px; height: 600px;
    color: var(--ink); font-family: "Montserrat", sans-serif; font-weight: 700;
  }
  .abs { position: absolute; }
  .section-title {
    position: absolute; font-family: "Jost", sans-serif; font-weight: 700;
    font-size: 29px; letter-spacing: 1.5px; text-align: center; transform: translateX(-50%);
    white-space: nowrap; line-height: 1;
  }
  .intro {
    position: absolute; text-align: center; font-size: 12.2px; line-height: 16.5px;
    transform: translateX(-50%); width: 260px;
  }
  .note {
    position: absolute; transform: translateX(-50%); white-space: nowrap;
    font-weight: 900; font-size: 15px; line-height: 1;
  }
  .item { position: absolute; width: 224px; }
  .item-row {
    display: flex; align-items: baseline; font-weight: 900; font-size: 14.5px;
    line-height: 1; white-space: nowrap;
  }
  .item-row .leader {
    flex: 1; border-bottom: 2.5px dotted var(--ink); margin: 0 2px 2px 4px;
  }
  .item-desc { font-size: 9.4px; line-height: 12.2px; margin-top: 4px; letter-spacing: -0.2px; }
  .bullet-dot { position: absolute; width: 8px; height: 8px; border-radius: 50%; background: var(--accent); }
  .pattern { position: absolute; background: var(--accent-soft); }
  .step-box {
    position: absolute; border: 2px solid var(--ink); width: 102px; height: 28px;
    font-weight: 900; font-size: 14px; display: flex; align-items: center; justify-content: center;
  }
  .choose { position: absolute; transform: translateX(-50%); font-weight: 900; font-size: 14.5px; white-space: nowrap; line-height: 1; }
  .option { position: absolute; font-size: 8.8px; line-height: 12.4px; width: 215px; letter-spacing: -0.25px; }
  .option b { font-weight: 900; }
  .brand {
    position: absolute; left: 1086px; top: 544px; width: 100px; text-align: center;
    font-weight: 800; font-size: 13px; line-height: 1.1; color: var(--ink);
  }
</style>
</head>
<body>
<main class="board">

  <!-- Beef burgers -->
  <h2 class="section-title" style="left:192px; top:54px;">BEEF BURGERS</h2>
  <p class="intro" style="left:192px; top:98px;">All our patties are 100% natural beef, we know because we grind it ourselves, smashed to order on a hot grill rite in front of you.</p>
  <p class="note" style="left:192px; top:182px;">• DOUBLE PATTY ADD 4 •</p>

  <span class="bullet-dot" style="left:36px; top:292px;"></span>
  <span class="bullet-dot" style="left:36px; top:307px;"></span>
  <span class="bullet-dot" style="left:36px; top:322px;"></span>

  <div class="item" style="left:84px; top:228px;">
    <div class="item-row"><span>CLASSIC BEEF</span><span class="leader"></span><span>8.9</span></div>
    <p class="item-desc">Shredded lettuce, sliced tomato, caramilised onions, beetroot and BBQ Sauce on a buttered sesame see bun.</p>
  </div>
  <div class="item" style="left:84px; top:291px;">
    <div class="item-row"><span>CHEESE BURGER</span><span class="leader"></span><span>9.5</span></div>
    <p class="item-desc">Dill pickles, minced onion, american cheese, mustard and ketchup on a soft milk bun.</p>
  </div>
  <div class="item" style="left:84px; top:338px;">
    <div class="item-row"><span>FLAME GRILL</span><span class="leader"></span><span>9.5</span></div>
    <p class="item-desc">Shredded lettuce, sliced tomato, minced onion, dill pickles, american cheese, mayo and ketchup on a soft milk bun.</p>
  </div>
  <div class="item" style="left:84px; top:400px;">
    <div class="item-row"><span>BIG MIC</span><span class="leader"></span><span>9.9</span></div>
    <p class="item-desc">Shredded lettuce, dill pickles, minced union, american cheese and special sauce on a soft milk bun.</p>
  </div>
  <div class="item" style="left:84px; top:463px;">
    <div class="item-row"><span>TRUFFLED</span><span class="leader"></span><span>9.9</span></div>
    <p class="item-desc">Rocket, caramelised union, dill pickles, harvati cheese and truffle infused mayo on soft milk bun.</p>
  </div>

  <!-- Chicken burgers -->
  <h2 class="section-title" style="left:486px; top:55px;">CHICKEN BURGERS</h2>
  <p class="intro" style="left:486px; top:98px;">All our chicken burger patties are prepared onsite daily using premium quality chicken breast.</p>
  <p class="note" style="left:486px; top:182px;">• DOUBLE PATTY ADD 4 •</p>

  <div class="item" style="left:379px; top:228px;">
    <div class="item-row"><span>CLASSIC CHICKEN</span><span class="leader"></span><span>8.9</span></div>
    <p class="item-desc">Shredded lettuce, cheese and mayo on a classic sesame seed bun.</p>
  </div>
  <div class="item" style="left:379px; top:281px;">
    <div class="item-row"><span>PIRRI PIRRI</span><span class="leader"></span><span>9.5</span></div>
    <p class="item-desc">Shredded lettuce, cheese, mayo and house made pirri pirri on a classic sesame seed bun.</p>
  </div>
  <div class="item" style="left:379px; top:335px;">
    <div class="item-row"><span>KENTUCKY</span><span class="leader"></span><span>9.9</span></div>
    <p class="item-desc">Shredded lettuce, swiss cheese and feisty mayo on a soft milk bun.</p>
  </div>
  <div class="item" style="left:379px; top:388px;">
    <div class="item-row"><span>EL BURGER</span><span class="leader"></span><span>9.9</span></div>
    <p class="item-desc">Shredded lettuce, salsa, guacamole, cheese and chipotle mayo on a classic sesame seed bun.</p>
  </div>

  <div class="pattern" role="img" aria-label="Pink zigzag line pattern" style="left:420px; top:485px; width:185px; height:50px;"></div>

  <!-- Decorative areas -->
  <div class="pattern" role="img" aria-label="Pink interlocking diamond outline ornament" style="left:699px; top:13px; width:116px; height:76px;"></div>
  <div class="pattern" role="img" aria-label="Pink zigzag line pattern" style="left:1016px; top:45px; width:184px; height:51px;"></div>
  <div class="pattern" role="img" aria-label="Scattered pink plus sign pattern" style="left:624px; top:147px; width:108px; height:91px;"></div>

  <!-- Sides -->
  <h2 class="section-title" style="left:912px; top:74px;">SIDES</h2>
  <div class="item" style="left:769px; top:122px; width:243px;">
    <div class="item-row"><span>FRIES</span><span class="leader"></span><span>3.5</span></div>
  </div>
  <div class="item" style="left:769px; top:147px; width:243px;">
    <div class="item-row"><span>KENTUCKY TENDERS</span><span class="leader"></span><span>6.9</span></div>
    <p class="item-desc">Breaded and fried chicken tenders with secret seasoning. (2 pcs)</p>
  </div>

  <!-- Nachos & loaded fries -->
  <h2 class="section-title" style="left:938px; top:213px; font-size:26px;">NACHOS &amp; LOADED FRIES</h2>
  <div class="step-box" style="left:741px; top:250px;">STEP ONE</div>
  <div class="step-box" style="left:1022px; top:250px;">STEP TWO</div>

  <p class="choose" style="left:790px; top:290px;">• CHOOSE EITHER •</p>
  <div class="item" style="left:693px; top:313px; width:217px;">
    <div class="item-row"><span>SEASONED FRIES</span><span class="leader"></span><span>9.9</span></div>
  </div>
  <p class="abs" style="left:693px; top:335px; font-weight:900; font-size:14.5px; line-height:1;">OR FRESHLY COOKED</p>
  <div class="item" style="left:693px; top:353px; width:220px;">
    <div class="item-row"><span>CORN CHIPS</span><span class="leader"></span><span>11.5</span></div>
  </div>

  <p class="choose" style="left:1079px; top:290px;">• CHOOSE ONE •</p>
  <p class="option" style="left:981px; top:312px;"><b>GUACAMOLE</b> Salsa fresca, guacamole, jalapenos, cheese sauce and sour cream.</p>
  <p class="option" style="left:981px; top:343px;"><b>BEEF CHILI</b> Salsa fresca, beef chili, jalapenos, cheese and sour cream.</p>

  <!-- Buffalo chicken ribs -->
  <h2 class="section-title" style="left:933px; top:397px; font-size:26px;">BUFFALO CHICKEN RIBS</h2>
  <p class="intro" style="left:918px; top:426px; width:470px;">Buffalo style fried chicken ribs smothered in one of our mouth-watering sauces, served with a side of ranch sauce.</p>

  <div class="item" style="left:744px; top:469px; width:145px;">
    <div class="item-row"><span>6 PACK</span><span class="leader"></span><span>6.9</span></div>
  </div>
  <div class="item" style="left:744px; top:488px; width:145px;">
    <div class="item-row"><span>12 PACK</span><span class="leader"></span><span>12.9</span></div>
  </div>
  <div class="item" style="left:744px; top:507px; width:147px;">
    <div class="item-row"><span>24 PACK</span><span class="leader"></span><span>23.9</span></div>
  </div>
  <p class="abs" style="left:940px; top:477px; font-weight:900; font-size:14.5px; line-height:19px;">CLASSIC HOT SAUCE<br>OR SMOKY BBQ</p>

  <p class="brand">harbor burger</p>
</main>
</body>
</html>
```